Mobile Fitness snd Therapy Business Card Design

I need a business card designed for my mobile fitness and therapy business.

Please view the images that I have uploaded. I like the simplicity of the design that I have attached. I adapted it with my information

Target Market(s)

Those seeking personal training, injury rehabilitation or massage therapy.

Industry/Entity Type

Business

Contact Information for Business Card

Dylan Marwick - MSc, CAT(C), RMT, CSCS, Pn2
e-mail: dylan@vantrelo.com
website: www.vantrelo.com
instagram: @dylan_marwick

Font styles to use
Sans Serif

Colors
3176b5
0355a3

Requirements
Must have
• "Contact us to receive a FREE assessment"
• Services offered:
• Personal Training
• Golf Fitness
• Injury Rehab
• Massage Therapy
• Yoga
Nice to have
• Consistent colours with brand
• - Dark Blue: #232837
• - Blue: #5096f0
• Consistent look/feel with the website: www.vantrelo.com

```html
<!DOCTYPE html>
<html lang="en">
<head>
<meta charset="utf-8">
<title>Vantrelo Business Card</title>
<link rel="stylesheet" href="https://fonts.googleapis.com/css2?family=Open+Sans:wght@400;600;700;800&display=swap">
<style>
  :root {
    --navy: #232837;
    --blue: #3176b5;
    --blue-deep: #0355a3;
    --paper: #ffffff;
    --backdrop: #e9eaed;
    --ink: #232837;
  }
  * { margin: 0; padding: 0; box-sizing: border-box; }
  html, body { width: 1200px; height: 1200px; overflow: hidden; }
  body {
    background: var(--backdrop);
    font-family: "Open Sans", Arial, sans-serif;
    display: flex;
    flex-direction: column;
    align-items: center;
    justify-content: center;
    gap: 80px;
  }
  .card {
    position: relative;
    width: 840px;
    height: 480px;
    box-shadow: 0 6px 24px rgba(35, 40, 55, 0.18);
  }
  .corner { position: absolute; width: 26px; height: 26px; }
  .corner.tl { top: 0; left: 0; }
  .corner.tr { top: 0; right: 0; }
  .corner.bl { bottom: 0; left: 0; }
  .corner.br { bottom: 0; right: 0; }

  /* Front */
  .card-front { background: var(--navy); display: flex; align-items: center; justify-content: center; }
  .card-front .corner { background: var(--paper); }
  .brand { text-align: left; color: var(--paper); }
  .brand-name {
    font-weight: 800;
    font-size: 92px;
    letter-spacing: 10px;
    line-height: 1;
  }
  .brand-tagline {
    font-weight: 700;
    font-size: 24px;
    letter-spacing: 6.4px;
    margin-top: 12px;
  }

  /* Back */
  .card-back { background: var(--paper); color: var(--ink); }
  .card-back .corner { background: var(--navy); }
  .back-brand { position: absolute; left: 58px; top: 56px; color: var(--navy); }
  .back-brand .brand-name { font-size: 46px; letter-spacing: 5px; }
  .back-brand .brand-tagline { font-size: 12px; letter-spacing: 3.2px; margin-top: 6px; }

  .person { position: absolute; left: 150px; top: 160px; }
  .person-name { font-weight: 700; font-size: 30px; line-height: 1.1; }
  .person-credentials { color: var(--blue); font-size: 14px; margin-top: 4px; }
  .contact-list { list-style: none; margin-top: 14px; }
  .contact-list li { display: flex; align-items: center; gap: 10px; font-size: 17px; line-height: 1.55; }
  .contact-list svg { width: 18px; height: 18px; flex: none; }

  .divider { position: absolute; left: 500px; top: 56px; width: 2px; height: 236px; background: var(--navy); }
  .services { position: absolute; left: 530px; top: 62px; }
  .services-title { font-weight: 700; font-size: 19px; margin-bottom: 6px; }
  .services-list { list-style: none; padding-left: 34px; }
  .services-list li { font-size: 17px; line-height: 1.6; }

  .cta {
    position: absolute; left: 0; right: 0; bottom: 52px;
    text-align: center; font-weight: 700; font-size: 26px; letter-spacing: 0.6px;
  }
</style>
</head>
<body>
  <section class="card card-front" aria-label="Card front">
    <span class="corner tl"></span><span class="corner tr"></span>
    <span class="corner bl"></span><span class="corner br"></span>
    <div class="brand">
      <div class="brand-name">VANTRELO</div>
      <div class="brand-tagline">NUTRITION - FITNESS - HEALTH</div>
    </div>
  </section>

  <section class="card card-back" aria-label="Card back">
    <span class="corner tl"></span><span class="corner tr"></span>
    <span class="corner bl"></span><span class="corner br"></span>

    <div class="brand back-brand">
      <div class="brand-name">VANTRELO</div>
      <div class="brand-tagline">NUTRITION - FITNESS - HEALTH</div>
    </div>

    <div class="person">
      <div class="person-name">Dylan Marwick</div>
      <div class="person-credentials">MSc, CAT(C), RMT, CSCS, Pn2</div>
      <ul class="contact-list">
        <li>
          <svg viewBox="0 0 18 18" aria-hidden="true"><rect x="1" y="3" width="16" height="12" fill="var(--blue-deep)"/><path d="M1 3 L9 10 L17 3" fill="none" stroke="#fff" stroke-width="1.5"/></svg>
          dylan@vantrelo.com
        </li>
        <li>
          <svg viewBox="0 0 18 18" aria-hidden="true"><circle cx="9" cy="9" r="8" fill="var(--blue-deep)"/><ellipse cx="9" cy="9" rx="3.5" ry="8" fill="none" stroke="#fff" stroke-width="1.2"/><line x1="1" y1="9" x2="17" y2="9" stroke="#fff" stroke-width="1.2"/></svg>
          www.vantrelo.com
        </li>
        <li>
          <svg viewBox="0 0 18 18" aria-hidden="true"><rect x="1" y="1" width="16" height="16" fill="var(--blue-deep)"/></svg>
          @dylan_marwick
        </li>
      </ul>
    </div>

    <div class="divider"></div>

    <div class="services">
      <div class="services-title">Services offered:</div>
      <ul class="services-list">
        <li>Personal Training</li>
        <li>Golf Fitness</li>
        <li>Injury Rehab</li>
        <li>Massage Therapy</li>
        <li>Yoga</li>
      </ul>
    </div>

    <p class="cta">“Contact us to receive a FREE assessment”</p>
  </section>
</body>
</html>
```